Sleek, Professional Business Card Design Needed

Business Cards - Logo Attached.

We are a solar consulting company. We are national and want our cards to represent the professional high quality products that we offer.

Industry/Entity Type

Business

Contact Information for Business Card

n/a

Requirements
Must have
• Design
• Name
• Position
• Number
• Email
• Address
Should not have
• Not be too crowded

```html
<!DOCTYPE html>
<html lang="en">
<head>
<meta charset="utf-8">
<title>Brightfield Energy – Business Cards</title>
<link rel="stylesheet" href="https://fonts.googleapis.com/css2?family=Lato:wght@400;700&display=swap">
<style>
  :root {
    --backdrop: #2a2a2a;
    --card: #ffffff;
    --card-shade: #f0f0f0;
    --brand-blue: #1f95cf;
    --brand-green: #8dc13f;
    --text-grey: #6b6b6b;
  }
  * { box-sizing: border-box; margin: 0; padding: 0; }
  html, body { width: 1200px; height: 1031px; overflow: hidden; }
  body {
    background: var(--backdrop);
    font-family: "Lato", sans-serif;
    position: relative;
  }
  .card {
    position: absolute;
    width: 520px;
    height: 300px;
    background: radial-gradient(ellipse at 50% 45%, var(--card) 55%, var(--card-shade) 100%);
    box-shadow: 0 14px 30px rgba(0,0,0,.55);
    overflow: hidden;
  }
  .card--front { left: 50px; top: 366px; }
  .card--back  { left: 630px; top: 366px; }

  /* brand lockup */
  .brand {
    display: flex;
    align-items: center;
    gap: 12px;
  }
  .brand__dot {
    width: 46px; height: 46px;
    border: 5px solid var(--brand-green);
    border-radius: 50%;
    flex: none;
  }
  .brand__name {
    color: var(--brand-blue);
    font-weight: 400;
    font-size: 24px;
    letter-spacing: .5px;
    text-transform: uppercase;
    line-height: 1.1;
    padding-bottom: 6px;
    border-bottom: 2px solid var(--brand-green);
  }

  .card--front .brand {
    position: absolute;
    left: 50%; top: 50%;
    transform: translate(-50%, -50%);
  }

  /* back */
  .card__tab {
    position: absolute;
    left: 0; top: 0;
    width: 62px; height: 42px;
    background: var(--brand-blue);
  }
  .card--back .brand {
    position: absolute;
    left: 56px; top: 36px;
  }
  .card--back .brand__name { font-size: 21px; }
  .person {
    position: absolute;
    left: 118px; top: 112px;
    width: 190px;
    padding-bottom: 8px;
    border-bottom: 1.5px solid var(--brand-green);
  }
  .person__name {
    color: var(--brand-blue);
    font-size: 19px;
    text-transform: uppercase;
    letter-spacing: .4px;
  }
  .person__role {
    color: var(--text-grey);
    font-size: 12px;
    margin-top: 2px;
  }
  .address {
    position: absolute;
    right: 26px; top: 34px;
    width: 160px;
    text-align: right;
    color: var(--text-grey);
    font-size: 11.5px;
    line-height: 1.5;
    padding-bottom: 8px;
    border-bottom: 1.5px solid var(--brand-green);
  }
  .contact {
    position: absolute;
    left: 26px; bottom: 30px;
    width: 200px;
    list-style: none;
    color: var(--text-grey);
    font-size: 11.5px;
    line-height: 1.6;
    padding-top: 8px;
    border-top: 1.5px solid var(--brand-green);
  }
  .contact li { display: flex; align-items: center; gap: 6px; }
  .contact svg { width: 10px; height: 10px; flex: none; }
  .card__band {
    position: absolute;
    left: 0; right: 0; bottom: 0;
    height: 10px;
    background: var(--brand-green);
  }
</style>
</head>
<body>
  <section class="card card--front" aria-label="Card front">
    <div class="brand">
      <span class="brand__dot"></span>
      <span class="brand__name">Brightfield Energy</span>
    </div>
  </section>

  <section class="card card--back" aria-label="Card back">
    <div class="card__tab"></div>
    <div class="brand">
      <span class="brand__dot"></span>
      <span class="brand__name">Brightfield Energy</span>
    </div>
    <div class="person">
      <p class="person__name">Martin Halloway</p>
      <p class="person__role">Managing Director</p>
    </div>
    <address class="address" style="font-style:normal">
      Elm Road, 48/B<br>Hartfield, HT3 2LP
    </address>
    <ul class="contact">
      <li>
        <svg viewBox="0 0 10 10" aria-hidden="true"><circle cx="5" cy="5" r="5" fill="#1f95cf"/><path d="M3.2 2.6c.3-.3.7-.2.8.1l.4.8c.1.2 0 .4-.2.5l-.3.2c.3.7.8 1.2 1.5 1.5l.2-.3c.1-.2.3-.3.5-.2l.8.4c.3.1.4.5.1.8-.6.6-1.6.6-2.5-.1-.9-.7-1.6-1.6-1.8-2.5-.1-.5 0-.9.5-1.2z" fill="#fff"/></svg>
        +1-404-555-0187
      </li>
      <li>
        <svg viewBox="0 0 10 10" aria-hidden="true"><rect x="0" y="2" width="10" height="7" fill="#1f95cf"/><path d="M0 2l5 4 5-4" fill="none" stroke="#fff" stroke-width="1"/></svg>
        hello@brightfieldenergy.com
      </li>
    </ul>
    <div class="card__band"></div>
  </section>
</body>
</html>
```